Product label design needed for an odor removal line of products.

I need a label designed for an odor removal product line. There are eight additional odor removal products that I will need labels designed for so the winner will have additional work from me. I would like each of those products to have a similar look and feel in each one. This contest is for one of the products. The Brightwell 417 (would love a better name if you are so inclined -many people know what it is by the 417). The no smell formula does not mask odors, it eliminates odors at their source . Also Reduces Allergens! Simply open silver packet and place in dispenser. Great for use in cars, near pet beds or litter boxes, near diaper pails -anywhere odors are a problem. Lasts 60-90 days. Safe to use. Other uses: Nursing homes, hotel rooms, locker rooms, teenage boy rooms, basements... Eco Friendly! No VOC's or phthalates! Do not consume. Keep out of reach of children and pets. Replace every 60-90 days. I put the picture of my logo , the product as it is packaged and a picture of the actual product and the dispenser it will go in. the package is 4x5 in silver packet with .25 seam on the side and .5 seam on the top and bottom. (Dispenser will have a label with reorder information on it. to be designed later) You do not have to put all information provided on the label. It is to be used as you see fit. I tend to like clean, bold designs but am open to all options. Prefer not to use word air freshener.

Target Market(s)

Men and women between 30-65

Industry/Entity Type

Cleaning Product

Font styles to use
Sans Serif

Colors
acd136
9bcb3c
ffffff

Requirements
Must have
• ability for concept/look to be used for a laundry product, smaller odor elimination pouch, odor removing canister and spray as well
Nice to have
• I like greens but am open to designers to decide
Should not have
• word air freshener

```html
<!DOCTYPE html>
<html lang="en">
<head>
<meta charset="utf-8">
<title>The Brightwell 417 – Label</title>
<link href="https://fonts.googleapis.com/css2?family=Montserrat:wght@800&family=Barlow:wght@500;600&family=Barlow+Semi+Condensed:wght@600&display=swap" rel="stylesheet">
<style>
  :root {
    --frame-grey: #58585a;
    --charcoal: #38383a;
    --paper: #ffffff;
    --leaf-green: #84c448;
    --badge-green: #9bcb3c;
  }
  * { margin: 0; padding: 0; box-sizing: border-box; }
  html, body { width: 1022px; height: 1200px; overflow: hidden; background: var(--frame-grey); }
  .label {
    position: relative;
    width: 1022px;
    height: 1200px;
    background: var(--frame-grey);
  }
  .label-art { position: absolute; inset: 0; }
  .brand-name {
    position: absolute;
    left: 311px; width: 400px;
    top: 404px;
    text-align: center;
    font-family: "Barlow", sans-serif;
    font-weight: 600;
    font-size: 40px;
    letter-spacing: 4px;
    line-height: 44px;
    color: var(--charcoal);
  }
  .product-title {
    position: absolute;
    left: 109px; width: 804px;
    top: 657px;
    text-align: center;
    font-family: "Montserrat", sans-serif;
    font-weight: 800;
    font-size: 76px;
    line-height: 80px;
    letter-spacing: -0.5px;
    color: var(--charcoal);
  }
  .claims {
    position: absolute;
    left: 175px; width: 672px;
    top: 880px;
    text-align: center;
    font-family: "Barlow Semi Condensed", sans-serif;
    font-weight: 600;
    font-size: 25px;
    line-height: 30px;
    color: var(--paper);
  }
  .notice {
    position: absolute;
    top: 944px;
    font-family: "Barlow", sans-serif;
    font-weight: 500;
    font-size: 31px;
    line-height: 35px;
    color: var(--paper);
  }
  .notice--safety { right: 518px; text-align: right; }
  .notice--replace { left: 564px; text-align: left; }
</style>
</head>
<body>
  <main class="label">
    <svg class="label-art" width="1022" height="1200" viewBox="0 0 1022 1200" aria-hidden="true">
      <rect class="panel" x="109" y="97" width="804" height="1005" fill="var(--paper)"/>
      <rect class="top-band" x="311" y="97" width="401" height="271" fill="var(--charcoal)"/>
      <circle class="emblem-backing" cx="511" cy="426" r="208" fill="var(--paper)"/>
      <circle class="emblem-disc" cx="511" cy="426" r="187" fill="var(--badge-green)"/>
      <polygon class="claims-ribbon" points="230,870 792,870 847,924 175,924" fill="var(--charcoal)"/>
      <rect class="footer-band" x="109" y="924" width="804" height="178" fill="var(--leaf-green)"/>
      <line class="footer-divider" x1="535" y1="946" x2="535" y2="1017" stroke="var(--paper)" stroke-width="4"/>
    </svg>

    <div class="brand-name">VERDANT<br>HAVEN</div>

    <h1 class="product-title">THE<br>BRIGHTWELL 417</h1>

    <p class="claims">Eco Friendly! &nbsp;| No VOC's or phthalates!</p>

    <p class="notice notice--safety">Keep out of reach of<br>children and pets.</p>
    <p class="notice notice--replace">Replace every<br>60-90 days</p>
  </main>
</body>
</html>
```